Business Cards and Stationery incorporating Logo design
Business Cards and Stationery incorporating Logo design -
Creative Brief
Professional
Daniel P. Halvorsen
Managing Director
418 Corvane Tower 9th Fl. Uniondale, NY 11553
1-555-hdg-cash
dhalvorsen@halvorsendrakeco.example
www.halvorsendrakeco.example

```html
<!DOCTYPE html>
<html lang="en">
<head>
<meta charset="utf-8">
<title>Halvorsen Drake — Business Cards</title>
<link rel="stylesheet" href="https://fonts.googleapis.com/css2?family=Cinzel:wght@400;700&display=swap">
<style>
  :root {
    --canvas: #e9e6e1;
    --card-white: #ffffff;
    --card-shade: #dcdcdc;
    --brand-green: #0d6b3a;
    --brand-dark: #231f20;
    --text-grey: #6d6d6d;
    --on-green: #ffffff;
  }
  * { box-sizing: border-box; margin: 0; padding: 0; }
  html, body { width: 1200px; height: 911px; overflow: hidden; }
  body {
    position: relative;
    background: var(--canvas);
    font-family: "Cinzel", serif;
  }
  .card {
    position: absolute;
    border-radius: 14px;
    box-shadow: 0 6px 14px rgba(0,0,0,.28);
  }
  .card--white { background: linear-gradient(180deg, var(--card-white) 55%, var(--card-shade)); }

  /* Front card */
  .card-front { left: 143px; top: 309px; width: 420px; height: 234px; }
  .front-brand {
    position: absolute; right: 22px; top: 18px;
    display: flex; flex-direction: column; align-items: flex-end;
  }
  .front-brand .brand-square { width: 72px; height: 72px; background: var(--brand-green); margin-right: 44px; }
  .front-brand .brand-name {
    margin-top: 6px; text-align: left;
    font-size: 24px; line-height: 1.02; font-weight: 700;
    color: var(--brand-dark); letter-spacing: .3px;
  }
  .front-brand .brand-name span { display: block; color: var(--brand-green); }
  .person { position: absolute; left: 24px; top: 124px; color: var(--text-grey); }
  .person-name { font-size: 15px; color: var(--brand-green); letter-spacing: .3px; }
  .person-title { font-size: 9px; margin-top: 3px; }
  .person-cell { font-size: 9px; margin-top: 2px; }
  .contact { position: absolute; left: 24px; top: 180px; font-size: 8.5px; line-height: 1.4; color: var(--text-grey); }

  /* Green back card */
  .card-back-green {
    left: 630px; top: 212px; width: 419px; height: 240px;
    background: var(--brand-green);
  }
  .green-brand {
    position: absolute; left: 50%; top: 46px; transform: translateX(-50%);
    display: flex; flex-direction: column; align-items: center; gap: 8px;
  }
  .green-brand .brand-square { width: 122px; height: 122px; background: var(--on-green); }
  .green-brand .brand-name { font-size: 13px; font-weight: 700; color: var(--on-green); letter-spacing: .5px; white-space: nowrap; }
  .card-back-green .web {
    position: absolute; left: 50%; bottom: 30px; transform: translateX(-50%);
    font-size: 8.5px; color: var(--on-green); white-space: nowrap;
  }

  /* White back card */
  .card-back-white { left: 363px; top: 514px; width: 420px; height: 234px; }
  .white-brand {
    position: absolute; left: 50%; top: 40px; transform: translateX(-50%);
    display: flex; flex-direction: column; align-items: center; gap: 8px;
  }
  .white-brand .brand-square { width: 124px; height: 124px; background: var(--brand-dark); }
  .white-brand .brand-name { font-size: 13px; font-weight: 700; color: var(--brand-green); letter-spacing: .5px; white-space: nowrap; }
  .card-back-white .web {
    position: absolute; left: 50%; bottom: 28px; transform: translateX(-50%);
    font-size: 8.5px; color: var(--text-grey); white-space: nowrap;
  }
</style>
</head>
<body>
  <section class="card card--white card-front">
    <div class="front-brand">
      <div class="brand-square"></div>
      <div class="brand-name">Halvorsen<span>Drake</span></div>
    </div>
    <div class="person">
      <div class="person-name">Daniel P. Halvorsen</div>
      <div class="person-title">Managing Director</div>
      <div class="person-cell">C: (555) 018 0408</div>
    </div>
    <div class="contact">
      <div>418 Corvane Tower 9th Fl. Brightwater, OR 97402</div>
      <div>T: 1-555-014-7720 &nbsp;|&nbsp; F: (555) 014-2290</div>
      <div>E: dhalvorsen@halvorsendrakeco.example</div>
      <div>W: www.halvorsendrakeco.example</div>
    </div>
  </section>

  <section class="card card-back-green">
    <div class="green-brand">
      <div class="brand-square"></div>
      <div class="brand-name">Halvorsen Drake</div>
    </div>
    <div class="web">www.halvorsendrakeco.example</div>
  </section>

  <section class="card card--white card-back-white">
    <div class="white-brand">
      <div class="brand-square"></div>
      <div class="brand-name">Halvorsen Drake</div>
    </div>
    <div class="web">www.halvorsendrakeco.example</div>
  </section>
</body>
</html>
```